New London based construction company website

We need a website designing for our new London based construction company which aims to provide total & fernway yard services.

The website is to have two sides to it one for "halcrest build services" and one for "fernway yard services" with an opening page with both logo's to choose from.

Would like the website to be modern, professional and inspire confidence.

Target Market(s)

Those specifically visiting the site to check that the company is professional

Industry/Entity Type

Construction

Contact Information for Business Card

One side for Fernway Yard Services the other Halcrest Build Services

Number of Pages Required

5+ page

Font styles to use
Sans Serif

Requirements
Must have
• The website is to have two sides to it one for "halcrest build services" and one for "fernway yard services" with an opening page with both logo's to choose from.

```html
<!DOCTYPE html>
<html lang="en">
<head>
<meta charset="utf-8">
<title>Fernway Yard Services</title>
<link href="https://fonts.googleapis.com/css2?family=Montserrat:wght@400;500;600;700&family=Open+Sans:wght@400;600;700&family=Cinzel:wght@400&display=swap" rel="stylesheet">
<style>
:root{
  --blue:#1b5ca3;
  --blue-deep:#0f4a8c;
  --ink:#1d1d1d;
  --text:#333;
  --muted:#888;
  --band:#eeeeee;
  --gallery:#7a7c7f;
  --footer:#3a3a3a;
  --footer-line:#555;
  --white:#fff;
}
*{box-sizing:border-box;margin:0;padding:0}
html,body{width:1200px;height:3468px;overflow:hidden}
body{position:relative;background:var(--white);font-family:"Open Sans",sans-serif;color:var(--text)}
.abs{position:absolute}
.photo{position:absolute}

/* header */
.site-header{left:0;top:0;width:1200px;height:111px;background:var(--white)}
.brand{left:69px;top:32px;display:flex;align-items:center;gap:14px}
.brand-mark{width:44px;height:44px;background:var(--blue)}
.brand-name{font-family:"Montserrat",sans-serif;font-weight:600;font-size:26px;color:var(--blue-deep);letter-spacing:1px;text-transform:uppercase}
.main-nav{left:612px;top:62px;display:flex}
.main-nav a{font-family:"Montserrat",sans-serif;font-size:13px;color:var(--ink);text-decoration:none;text-transform:uppercase;margin-right:41px;padding-bottom:15px;position:relative}
.main-nav a:last-child{margin-right:0}
.main-nav a.active::after{content:"";position:absolute;left:0;right:0;bottom:0;height:2px;background:var(--blue)}

/* hero */
.hero{left:0;top:111px;width:1200px;height:610px;
  background:
    radial-gradient(ellipse 190px 300px at 890px 420px,rgba(250,250,252,.95),rgba(250,250,252,0)),
    radial-gradient(ellipse 170px 280px at 560px 420px,rgba(245,247,250,.9),rgba(245,247,250,0)),
    radial-gradient(ellipse 420px 230px at 250px 430px,rgba(70,78,90,.75),rgba(70,78,90,0)),
    radial-gradient(ellipse 260px 180px at 480px 170px,rgba(214,170,60,.35),rgba(214,170,60,0)),
    linear-gradient(180deg,#c9ced6 0%,#b9c0c9 45%,#8f969f 100%)}
.feature-band{left:0;top:721px;width:1200px;height:308px;background:var(--band)}
.feature-img{top:620px;width:302px;height:178px}
.feature-title{top:836px;font-family:"Montserrat",sans-serif;font-weight:700;font-size:18px;color:var(--ink);text-transform:uppercase}
.feature-text{top:868px;width:300px;font-size:13px;line-height:21px;color:var(--text)}
.read-more{top:942px;font-size:12px;font-weight:700;color:var(--blue-deep);text-transform:uppercase}

/* about */
.about-img{left:134px;top:1179px;width:492px;height:324px;background:linear-gradient(180deg,#dbe4ee 0%,#b9c6d4 45%,#5f7088 100%)}
.about-box{left:550px;top:1142px;width:490px;height:389px;background:var(--blue);color:var(--white);padding:72px 60px 0 116px}
.about-box h2{font-family:"Cinzel",serif;font-weight:400;font-size:33px;letter-spacing:1px;margin-bottom:28px}
.about-box p{font-size:13px;line-height:21px;margin-bottom:20px}

/* gallery */
.gallery{left:0;top:1628px;width:1200px;height:783px;background:var(--gallery)}
.section-title{left:0;width:1200px;text-align:center;font-family:"Montserrat",sans-serif;font-weight:600;font-size:35px;text-transform:uppercase}
.gallery .section-title{top:58px;color:var(--white)}
.tile{width:234px;height:255px;border-radius:3px}
.tile-feature{background:var(--blue);display:flex;flex-direction:column;align-items:center;justify-content:center;gap:16px}
.tile-btn{border:1px solid var(--white);color:var(--white);font-size:14px;padding:4px 18px;border-radius:3px}

/* clients */
.clients-title{top:2466px;color:#2b2b2b}
.avatar{left:538px;top:2545px;width:140px;height:140px;border-radius:50%;border:4px solid #ddd;background:linear-gradient(180deg,#e9e9e9,#9a9a9a)}
.client-name{left:0;top:2705px;width:1200px;text-align:center;font-family:"Montserrat",sans-serif;font-weight:700;font-size:22px;color:#444}
.client-quote{left:240px;top:2755px;width:740px;text-align:center;font-size:13px;line-height:30px;color:var(--muted)}
.dots{left:560px;top:2836px;display:flex;gap:14px;align-items:center}
.dot{width:12px;height:12px;border-radius:50%;background:#222}
.dot.on{width:22px;height:22px;background:#2a52d6;border:3px solid #c5d0f5}

/* skyline */
.skyline{left:0;top:2878px;width:1200px;height:139px;background:linear-gradient(180deg,#fff 0%,#fff 15%,#4a4a4a 60%,#3a3a3a 100%)}

/* footer */
.footer{left:0;top:3017px;width:1200px;height:409px;background:var(--footer);color:#ddd}
.footer h3{top:52px;font-family:"Montserrat",sans-serif;font-weight:600;font-size:20px;color:var(--white)}
.footer h3::after{content:"";display:block;width:40px;height:1px;background:#888;margin-top:12px}
.footer-about{left:81px;top:118px;width:262px;font-size:12px;line-height:22px;color:#ddd}
.worker{width:72px;height:64px;background:linear-gradient(180deg,#c9b999,#6d7a8a)}
.sub-text{left:615px;top:116px;width:240px;font-size:12px;line-height:26px}
.sub-input{left:615px;top:183px;width:232px;height:38px;background:#222;color:#ddd;font-size:11px;padding:12px 14px}
.sub-btn{left:615px;top:245px;width:80px;height:28px;background:var(--blue);color:var(--white);font-size:11px;text-align:center;line-height:28px}
.contact-row{left:874px;width:232px;font-size:14px;display:flex;gap:14px;border-bottom:1px solid var(--footer-line);padding-bottom:12px;line-height:22px}
.contact-row svg{flex:none;margin-top:4px}
.footer-rule{left:81px;top:345px;width:1036px;height:1px;background:var(--footer-line)}
.footer-nav{left:92px;top:366px;display:flex;font-size:10px;text-transform:uppercase;color:#eee}
.footer-nav span{padding:0 12px;border-left:1px solid #aaa}
.footer-nav span:first-child{padding-left:0;border-left:0}
.social{left:955px;top:358px;display:flex;gap:10px}
.social i{width:26px;height:26px;border:1px solid #ccc;border-radius:50%;display:block}
.copyright{left:0;top:3426px;width:1200px;height:42px;background:var(--blue-deep);color:#e6e6e6;font-size:12px;padding:13px 0 0 84px}
</style>
</head>
<body>

<header class="site-header abs">
  <div class="brand abs"><span class="brand-mark"></span><span class="brand-name">Fernway Yard Services</span></div>
  <nav class="main-nav abs">
    <a class="active">Home</a><a>About</a><a>Services</a><a>Gallery</a><a>Contact Us</a>
  </nav>
</header>

<div class="hero photo" role="img" aria-label="Two engineers in white shirts and hard hats shaking hands in front of a steel-framed building under construction, with tower cranes and birds against a pale sky"></div>

<section class="feature-band abs"></section>
<div class="feature-img photo" style="left:97px;background:linear-gradient(180deg,#cfd8e2,#6b7581)" role="img" aria-label="Steel frame of a tower under construction"></div>
<div class="feature-img photo" style="left:439px;background:linear-gradient(180deg,#e6e2dc,#8c8075)" role="img" aria-label="Team reviewing plans on site"></div>
<div class="feature-img photo" style="left:802px;background:linear-gradient(180deg,#d7dde4,#b9743f)" role="img" aria-label="Orange excavator on a dirt site"></div>

<h3 class="feature-title abs" style="left:97px">Temporty Teamwork</h3>
<h3 class="feature-title abs" style="left:439px">The Effective Teamwork</h3>
<h3 class="feature-title abs" style="left:802px">The Effective Teamwork</h3>
<p class="feature-text abs" style="left:97px">Constructor explains how you can enjoy high end flooring trends like textured wood and realistic stones with new laminate flooring.</p>
<p class="feature-text abs" style="left:439px">Constructor explains how you can enjoy high end flooring trends like textured wood and realistic stones with new laminate flooring.</p>
<p class="feature-text abs" style="left:802px">Constructor explains how you can enjoy high end flooring trends like textured wood and realistic stones with new laminate flooring.</p>
<span class="read-more abs" style="left:97px">Read More</span>
<span class="read-more abs" style="left:439px">Read More</span>
<span class="read-more abs" style="left:802px">Read More</span>

<div class="about-img photo" role="img" aria-label="Four builders in yellow hard hats studying a blueprint"></div>
<section class="about-box abs">
  <h2>About Company</h2>
  <p>Constructor explains how you can enjoy high end flooring trends like textured wood and realistic stones with new laminate flooring.</p>
  <p>Constructor explains how you can enjoy high end flooring trends like textured wood Constructor explains how you can enjoy high end flooring trends like textured wood and realistic stones with new laminate flooring.</p>
</section>

<section class="gallery abs">
  <h2 class="section-title abs">Our Projects Gallery</h2>
  <div class="tile tile-feature abs" style="left:90px;top:152px">
    <svg width="28" height="28" viewBox="0 0 28 28" fill="none" stroke="#fff" stroke-width="2"><path d="M3 10V3h7M3 3l8 8M25 10V3h-7M25 3l-8 8M3 18v7h7M3 25l8-8M25 18v7h-7M25 25l-8-8"/></svg>
    <span class="tile-btn">Read More</span>
  </div>
  <div class="tile photo" style="left:351px;top:152px;background:linear-gradient(180deg,#b9c9dc,#6f6650)" role="img" aria-label="Worker holding a hard hat with tool belt"></div>
  <div class="tile photo" style="left:613px;top:152px;background:linear-gradient(180deg,#d5d9dd,#8d9399)" role="img" aria-label="Engineer pointing at plant machinery"></div>
  <div class="tile photo" style="left:872px;top:152px;background:linear-gradient(180deg,#c9d1d8,#4d5a6a)" role="img" aria-label="Engineers leaning over plans on a table"></div>
  <div class="tile photo" style="left:90px;top:437px;background:linear-gradient(180deg,#e7e3de,#a69685)" role="img" aria-label="Hands drawing on architectural plans"></div>
  <div class="tile photo" style="left:351px;top:437px;background:linear-gradient(180deg,#5f8fc4,#b8a83c)" role="img" aria-label="Site workers in hi-vis vests beneath a crane"></div>
  <div class="tile photo" style="left:613px;top:437px;background:linear-gradient(180deg,#b7d2ea,#8fa86a)" role="img" aria-label="Newly built detached house on a lawn"></div>
  <div class="tile photo" style="left:872px;top:437px;background:linear-gradient(180deg,#d9b46a,#6e5340)" role="img" aria-label="Finished living room interior with warm lighting"></div>
</section>

<h2 class="section-title clients-title abs">Our Clients</h2>
<svg class="abs" style="left:228px;top:2630px" width="52" height="90" viewBox="0 0 52 90" fill="none" stroke="#ccc" stroke-width="2"><path d="M48 2L4 45l44 43"/></svg>
<svg class="abs" style="left:952px;top:2630px" width="52" height="90" viewBox="0 0 52 90" fill="none" stroke="#ccc" stroke-width="2"><path d="M4 2l44 43L4 88"/></svg>
<div class="avatar photo" role="img" aria-label="Client portrait"></div>
<div class="client-name abs">Marcus Hale</div>
<p class="client-quote abs">Climb Leg Rub Face On Everything Give Attitude Nap All Day For Under The Bed. Chase Mice Attack Feet But Rub Face On Everything Hopped Up On Goofballs.</p>
<div class="dots abs"><span class="dot on"></span><span class="dot"></span><span class="dot"></span><span class="dot"></span></div>

<div class="skyline photo" role="img" aria-label="Dark city skyline silhouette of houses and tower blocks"></div>

<footer class="footer abs">
  <p class="footer-about abs">Sed Ut Perspiciatis Unde Omnis Iste Natus Error Sit Voluptatem Quae Ab Illo Inventore. Vitae Dicta Sunt Explicabo.Voluptatem Quae Ab Illo Inventore Nemo Enim Ipsam. Vitae Dicta Sunt Explicabo. Nemo Enim Ipsam..</p>

  <h3 class="abs" style="left:354px">Our Workers</h3>
  <div class="worker photo" style="left:354px;top:128px" role="img" aria-label="Worker photo"></div>
  <div class="worker photo" style="left:433px;top:128px" role="img" aria-label="Worker photo"></div>
  <div class="worker photo" style="left:512px;top:128px" role="img" aria-label="Worker photo"></div>
  <div class="worker photo" style="left:354px;top:200px" role="img" aria-label="Worker photo"></div>
  <div class="worker photo" style="left:433px;top:200px" role="img" aria-label="Worker photo"></div>
  <div class="worker photo" style="left:512px;top:200px" role="img" aria-label="Worker photo"></div>

  <h3 class="abs" style="left:615px">Subscribe Us</h3>
  <p class="sub-text abs">Aliquam Pulvinar Eros Vel Sem Ultrices, Ac Eleifend Libero Molestie.</p>
  <div class="sub-input abs">Your Email</div>
  <div class="sub-btn abs">subscribe</div>

  <h3 class="abs" style="left:874px">Contact Us</h3>
  <div class="contact-row abs" style="top:116px">
    <svg width="14" height="12" viewBox="0 0 14 12"><rect x="0" y="1" width="14" height="10" fill="#ddd"/><path d="M0 1l7 5 7-5" stroke="#3a3a3a" fill="none"/></svg><span>hello@fernwayyard.com</span></div>
  <div class="contact-row abs" style="top:163px">
    <svg width="14" height="14" viewBox="0 0 14 14"><path d="M3 0l3 3-2 2c1 2 3 4 5 5l2-2 3 3-2 3C6 14 0 8 0 3z" fill="#ddd"/></svg><span>020-555-0148</span></div>
  <div class="contact-row abs" style="top:210px;font-size:13px">
    <svg width="12" height="16" viewBox="0 0 12 16"><path d="M6 0a6 6 0 0 1 6 6c0 4-6 10-6 10S0 10 0 6a6 6 0 0 1 6-6z" fill="#ddd"/><circle cx="6" cy="6" r="2" fill="#3a3a3a"/></svg><span>48 Wharf Lane, Deptford<br>London SE8 3PT</span></div>

  <div class="footer-rule abs"></div>
  <nav class="footer-nav abs"><span>Home</span><span>About Us</span><span>Projects Area</span><span>Our Team</span><span>Contact Us</span></nav>
  <div class="social abs"><i></i><i></i><i></i><i></i><i></i></div>
</footer>

<div class="copyright abs">©2017 Fernway Yard Services . CA | All Right Reserved</div>

</body>
</html>
```